Banner for Vet Hospital 5m x 1.2m - Heat Stroke

Meadowlark Pet Hospital needs a Heat Stroke Banner for Summer.
The banner will be 5000mm long and 1200mm tall.

Our region has been hot this year and this summer is going to be extremely hot.
I want to warn people about heat stroke.
I want you to create a heat stroke banner that conveys the symptoms of heat stroke.

Pictures are better than words.
There should be IMAGES and WORDS that can be seen from the road 30m away and maybe some smaller words for people to read as they walk past.

Here are some of the signs of Heat Stroke:
- Panting which increases as heatstroke progresses
- Drooling, salivating
- Agitation, restlessness
- Very red or pale gums
- Bright red tongue
- Increased heart rate
- Breathing distress
- Vomiting Diarrhea (possibly with blood)
- Signs of mental confusion, delirium
- Dizziness, staggering
- Lethargy, weakness
- Muscle tremors
- Seizures
- Collapsing and lying down
- Little to no urine production
- Coma

I have attached characters that we often use in our advertising. They are optional.
I have done a mock up of the design I imagine. You could refine this design or make your own....or both.

Target Market(s)

Women aged 20 to 50.

Industry/Entity Type

Veterinary

Font styles to use
Sans Serif

Colors
fbed22
f78f20
ec1f27
ffffff

Requirements
Must have
• Heat Stroke Symtpms.
• Heat Stroke Warning.
• Summer theme.
Nice to have
• Bright colours.

```html
<!DOCTYPE html>
<html lang="en">
<head>
<meta charset="utf-8">
<title>Meadowlark Pet Hospital – Heat Stroke Banner</title>
<link rel="stylesheet" href="https://fonts.googleapis.com/css2?family=Anton&family=Oswald:wght@500;600;700&display=swap">
<style>
  :root {
    --page: #ffffff;
    --heat-start: #ff8c00;
    --heat-mid: #ff5a00;
    --heat-end: #ff0a0a;
    --ink: #ffffff;
    --logo-ink: #4a3a2a;
    --shadow: rgba(120, 20, 0, 0.45);
    --tone-orange: #ff7a10;
    --tone-amber: #ff5c05;
    --tone-flame: #ff3a08;
    --tone-red: #ff1a0a;
  }
  html, body {
    margin: 0;
    width: 1200px;
    height: 800px;
    overflow: hidden;
    background: var(--page);
  }
  .canvas {
    position: relative;
    width: 1200px;
    height: 800px;
  }
  .banner {
    position: absolute;
    left: 51px;
    top: 242px;
    width: 1097px;
    height: 262px;
    background: linear-gradient(90deg, var(--heat-start) 0%, var(--heat-mid) 45%, var(--heat-end) 100%);
    overflow: hidden;
  }

  /* Symptom pictures: white discs carrying the pet silhouette artwork */
  .pet-figure {
    position: absolute;
    width: 138px;
    height: 138px;
    border-radius: 50%;
    box-shadow: 0 2px 6px var(--shadow);
  }
  .pet-figure.panting  { left: 153px; top: 117px; background: linear-gradient(135deg, var(--ink) 0%, var(--ink) 30%, var(--tone-orange) 58%, var(--ink) 86%); }
  .pet-figure.drooling { left: 397px; top: 117px; background: linear-gradient(135deg, var(--ink) 0%, var(--tone-amber) 40%, var(--tone-amber) 55%, var(--ink) 80%); }
  .pet-figure.collapse { left: 648px; top: 117px; background: linear-gradient(120deg, var(--ink) 0%, var(--ink) 22%, var(--tone-flame) 45%, var(--tone-flame) 70%, var(--ink) 92%); }
  .pet-figure.cat      { left: 914px; top: 117px; background: linear-gradient(150deg, var(--ink) 0%, var(--ink) 25%, var(--tone-red) 50%, var(--tone-red) 68%, var(--ink) 90%); }

  .headline {
    position: absolute;
    left: 0;
    top: 0;
    width: 1097px;
    height: 140px;
  }
  .headline text {
    font-family: "Anton", "Oswald", sans-serif;
    font-size: 128px;
    fill: var(--ink);
    filter: drop-shadow(0 2px 3px var(--shadow));
  }

  .brand {
    position: absolute;
    left: 36px;
    top: 147px;
    width: 90px;
    height: 90px;
    border-radius: 50%;
    background: var(--ink);
    display: flex;
    align-items: center;
    justify-content: center;
    text-align: center;
  }
  .brand-name {
    font-family: "Oswald", sans-serif;
    font-weight: 600;
    font-size: 11px;
    line-height: 1.2;
    color: var(--logo-ink);
    text-transform: uppercase;
  }

  .symptoms {
    position: absolute;
    top: 143px;
    width: 140px;
    margin: 0;
    padding: 0;
    list-style: none;
    text-align: center;
    font-family: "Oswald", sans-serif;
    font-weight: 700;
    font-size: 17px;
    line-height: 20px;
    color: var(--ink);
    text-shadow: 0 1px 2px var(--shadow);
  }
  .symptoms.group-one { left: 273px; }
  .symptoms.group-two { left: 521px; top: 141px; line-height: 21px; }
  .symptoms .lead {
    font-size: 20px;
    line-height: 24px;
  }

  .call-to-action {
    position: absolute;
    left: 780px;
    top: 142px;
    width: 140px;
    text-align: center;
    font-family: "Oswald", sans-serif;
    font-weight: 700;
    color: var(--ink);
    text-shadow: 0 1px 2px var(--shadow);
  }
  .call-to-action .question {
    margin: 0;
    font-size: 16px;
    line-height: 17px;
  }
  .call-to-action .call-now {
    margin: 5px 0 0;
    font-size: 20px;
    line-height: 22px;
  }
  .call-to-action .phone {
    margin: 0;
    font-size: 21px;
    line-height: 22px;
    letter-spacing: 0.5px;
  }
</style>
</head>
<body>
<div class="canvas">
  <section class="banner" aria-label="Heat stroke warning banner">
    <div class="pet-figure panting" role="img" aria-label="Picture: panting dog silhouette with a sweat drop, cut into a white circle"></div>
    <div class="pet-figure drooling" role="img" aria-label="Picture: drooling dog silhouette with heavy breathing lines, cut into a white circle"></div>
    <div class="pet-figure collapse" role="img" aria-label="Picture: vomiting, staggering dog silhouette, cut into a white circle"></div>
    <div class="pet-figure cat" role="img" aria-label="Picture: collapsed cat silhouette with dazed eyes, cut into a white circle"></div>

    <svg class="headline" viewBox="0 0 1097 140" aria-label="Heat stroke can kill">
      <text x="41" y="124" textLength="1012" lengthAdjust="spacingAndGlyphs">HEAT STROKE CAN KILL</text>
    </svg>

    <div class="brand">
      <span class="brand-name">Meadowlark<br>Pet<br>Hospital</span>
    </div>

    <ul class="symptoms group-one">
      <li class="lead">EXCESSIVE</li>
      <li>panting</li>
      <li>drooling</li>
      <li>agitation</li>
      <li>breathing</li>
    </ul>

    <ul class="symptoms group-two">
      <li>diorrhea</li>
      <li>vomiting</li>
      <li>confusion</li>
      <li>tremours</li>
      <li>collapse+coma</li>
    </ul>

    <div class="call-to-action">
      <p class="question">noticed any<br>of these<br>symptoms?</p>
      <p class="call-now">CALL NOW!</p>
      <p class="phone">65550182</p>
    </div>
  </section>
</div>
</body>
</html>
```